Dalwin Electric Supply, Inc. Business Card Design

We are an Electrical Distributor looking for a Modern, Professional Business Card design.

Target Market(s)

Residential Commercial Industrial

Industry/Entity Type

Electrical

Contact Information for Business Card

Dalwin Electric Supply, Inc.
418 Tallow Creek Road
Brennick, NC 27514
555-312-4867
555-312-4921 Fax
dalwinelectric@voltmail.example

```html
<!DOCTYPE html>
<html lang="en">
<head>
<meta charset="utf-8">
<title>Dalwin Electric Supply, Inc. — Business Card</title>
<link rel="stylesheet" href="https://fonts.googleapis.com/css2?family=Questrial&display=swap">
<style>
  :root {
    --backdrop: #d6d6d6;
    --card-dark: #3b3b3d;
    --card-dark-deep: #2c2c2e;
    --card-light: #f4f4f4;
    --ink-dark: #4a4a4c;
    --ink-mid: #6b6b6d;
    --ink-light: #d8d8d8;
    --warm-start: #e2c318;
    --warm-end: #ea5f2b;
    --cool-start: #1c7a36;
    --cool-end: #1b7ac4;
  }
  * { margin: 0; padding: 0; box-sizing: border-box; }
  html, body { width: 1200px; height: 900px; overflow: hidden; }
  body {
    background: var(--backdrop);
    font-family: "Questrial", "Century Gothic", sans-serif;
    position: relative;
  }
  .card {
    position: absolute;
    left: 320px;
    width: 560px;
    height: 320px;
    border-radius: 4px;
    overflow: hidden;
    box-shadow: 0 10px 30px rgba(0,0,0,0.25);
  }
  .card--front { top: 70px; background: linear-gradient(160deg, var(--card-dark) 0%, var(--card-dark-deep) 100%); }
  .card--back { top: 510px; background: var(--card-dark-deep); }

  .brand {
    position: absolute;
    display: flex;
    align-items: center;
    gap: 12px;
    white-space: nowrap;
  }
  .brand__mark { width: 16px; height: 16px; flex: none; }
  .brand__name { font-size: 26px; letter-spacing: 0.5px; }
  .card--front .brand { left: 90px; top: 132px; }
  .card--front .brand__name { color: var(--ink-light); }
  .card--front .brand__mark { background: var(--ink-light); }

  .band { position: absolute; left: 0; right: 0; bottom: 0; height: 24px; }
  .band--warm { background: linear-gradient(90deg, var(--warm-start), var(--warm-end)); }
  .band--cool { background: linear-gradient(90deg, var(--cool-start), var(--cool-end)); }

  .back__top {
    position: absolute; left: 0; top: 0; right: 0; height: 176px;
    background: var(--card-light);
  }
  .card--back .brand { right: 30px; top: 42px; }
  .card--back .brand__name { font-size: 22px; color: var(--ink-dark); }
  .card--back .brand__mark { background: var(--ink-dark); width: 14px; height: 14px; }

  .person { position: absolute; left: 34px; top: 112px; }
  .person__name { font-size: 19px; letter-spacing: 1.5px; color: var(--ink-dark); font-weight: 400; -webkit-text-stroke: 0.5px var(--ink-dark); }
  .person__role { font-size: 15px; color: var(--ink-mid); margin-top: 4px; letter-spacing: 0.5px; }

  .address {
    position: absolute; right: 30px; top: 194px;
    text-align: right; color: var(--ink-light); font-size: 14px; line-height: 1.45; font-style: normal;
  }
  .contact { position: absolute; left: 34px; top: 218px; list-style: none; color: #bdbdbd; font-size: 13px; }
  .contact__item { display: flex; align-items: center; gap: 9px; line-height: 22px; }
  .contact__icon { width: 14px; height: 14px; flex: none; }
</style>
</head>
<body>
  <section class="card card--front" aria-label="Card front">
    <div class="brand">
      <span class="brand__mark"></span>
      <span class="brand__name">Dalwin Electric Supply, Inc.</span>
    </div>
    <div class="band band--warm"></div>
  </section>

  <section class="card card--back" aria-label="Card back">
    <div class="back__top"></div>
    <div class="brand">
      <span class="brand__mark"></span>
      <span class="brand__name">Dalwin Electric Supply, Inc.</span>
    </div>
    <div class="person">
      <h1 class="person__name">JORDAN HALE</h1>
      <p class="person__role">General Manager</p>
    </div>
    <address class="address">418 Tallow Creek Road<br>Brennick, NC 27514</address>
    <ul class="contact">
      <li class="contact__item">
        <svg class="contact__icon" viewBox="0 0 14 14"><rect x="0.5" y="0.5" width="13" height="13" rx="2" fill="#bdbdbd"/><rect x="4.5" y="2.5" width="5" height="9" rx="1" fill="none" stroke="#2c2c2e" stroke-width="1.2"/></svg>
        <span>555-312-4867</span>
      </li>
      <li class="contact__item">
        <svg class="contact__icon" viewBox="0 0 14 14"><rect x="0.5" y="0.5" width="13" height="13" rx="2" fill="#bdbdbd"/><path d="M4 3 L6 3 L6.5 5 L5.5 6 Q6.5 8 8 8.5 L9 7.5 L11 8 L11 10 Q6 11 3 4 Z" fill="#2c2c2e"/></svg>
        <span>555-312-4921 Fax</span>
      </li>
      <li class="contact__item">
        <svg class="contact__icon" viewBox="0 0 14 14"><rect x="0.5" y="0.5" width="13" height="13" rx="2" fill="#bdbdbd"/><rect x="3" y="4" width="8" height="6" fill="none" stroke="#2c2c2e" stroke-width="1.1"/><path d="M3 4 L7 7.5 L11 4" fill="none" stroke="#2c2c2e" stroke-width="1.1"/></svg>
        <span>dalwinelectric@voltmail.example</span>
      </li>
    </ul>
    <div class="band band--cool"></div>
  </section>
</body>
</html>
```